Wine Label Design

We need a wine label design with the following characteristics:
- Round
- I've attached a photo of a rough design
- The writing:
--- Four Rooks
---Crafted by Tal Venrick
-----Brambleway Chardonnay
------Dundee Hills
-----2021
- We'd like a couple of options on the background color:
- Pale mint green
- Cream
- Lettering a dark gray
- The three cursive Ms should kinda look like mountains
- Size: 3"x3"

```html
<!DOCTYPE html>
<html lang="en">
<head>
<meta charset="utf-8">
<title>Four Rooks – Brambleway Chardonnay Label</title>
<link rel="stylesheet" href="https://fonts.googleapis.com/css2?family=Fira+Sans+Condensed:wght@700&family=Source+Serif+4:opsz,wght@8..60,700&display=swap">
<style>
  :root {
    --backdrop: #efefef;
    --label-mint: #c3e5d6;
    --ink-gray: #3a3a3a;
  }
  html, body {
    margin: 0;
    padding: 0;
    width: 1200px;
    height: 900px;
    overflow: hidden;
    background: var(--backdrop);
  }
  .canvas {
    width: 1200px;
    height: 900px;
    display: flex;
    align-items: center;
    justify-content: center;
  }
  .wine-label {
    width: 660px;
    height: 660px;
    display: block;
  }
  .label-face { fill: var(--label-mint); }
  .label-ring {
    fill: none;
    stroke: var(--ink-gray);
    stroke-width: 4;
  }
  .arc-text {
    font-family: "Fira Sans Condensed", "Arial Narrow", sans-serif;
    font-weight: 700;
    font-size: 30px;
    letter-spacing: 0.5px;
    fill: var(--ink-gray);
    text-transform: uppercase;
  }
  .brand-name {
    font-family: "Fira Sans Condensed", "Arial Narrow", sans-serif;
    font-weight: 700;
    font-size: 46px;
    letter-spacing: 1px;
    fill: var(--ink-gray);
  }
  .vintage-year {
    font-family: "Source Serif 4", Georgia, serif;
    font-weight: 700;
    font-size: 104px;
    fill: var(--ink-gray);
  }
</style>
</head>
<body>
  <main class="canvas">
    <svg class="wine-label" viewBox="0 0 660 660" role="img" aria-label="Round wine label for Four Rooks Brambleway Chardonnay, Dundee Hills 2021">
      <defs>
        <path id="arc-top" d="M65,330 A265 265 0 0 1 595,330"/>
        <path id="arc-right" d="M376,69 A265 265 0 0 1 500,533"/>
        <path id="arc-bottom" d="M81,474 A288 288 0 0 0 579,474"/>
        <path id="arc-left" d="M127,500 A265 265 0 0 1 127,160"/>
      </defs>

      <circle class="label-face" cx="330" cy="330" r="330"/>
      <circle class="label-ring" cx="330" cy="330" r="304"/>

      <text class="arc-text winery-name">
        <textPath href="#arc-top" startOffset="50%" text-anchor="middle">Four Rooks</textPath>
      </text>
      <text class="arc-text winemaker-credit">
        <textPath href="#arc-right" startOffset="50%" text-anchor="middle">Crafted by Tal Venrick</textPath>
      </text>
      <text class="arc-text wine-name">
        <textPath href="#arc-bottom" startOffset="50%" text-anchor="middle">Brambleway Chardonnay</textPath>
      </text>
      <text class="arc-text region-name">
        <textPath href="#arc-left" startOffset="50%" text-anchor="middle">Dundee Hills</textPath>
      </text>

      <text class="brand-name" x="330" y="272" text-anchor="middle">FOUR ROOKS</text>
      <text class="vintage-year" x="330" y="412" text-anchor="middle">2021</text>
    </svg>
  </main>
</body>
</html>
```